New Business Card Design Project

Would like you to take my logo and create a business card much like the Bramblecove leasing.
I can get you the fonts used for the back of the card.
I want the same speckled blue with my logo on it.

Feel free to improve upon the balloon part of the logo if you can.
I put one I was doing with a new balloon and a more "string-like" "I".

```html
<!DOCTYPE html>
<html lang="en">
<head>
<meta charset="utf-8">
<title>Marigold Real Estate – Business Card</title>
<link href="https://fonts.googleapis.com/css2?family=Cinzel:wght@500&family=Open+Sans:wght@400;600&display=swap" rel="stylesheet">
<style>
  :root {
    --page-bg: #e9e9ec;
    --navy-deep: #0b1756;
    --navy: #14246e;
    --blue-bright: #2f63c4;
    --balloon-green: #7dc642;
    --name-green: #5cb531;
    --paper: #ffffff;
    --ink-grey: #6b6f78;
    --soft-white: #dfe6f5;
  }
  * { box-sizing: border-box; margin: 0; padding: 0; }
  html, body {
    width: 1200px; height: 1000px; overflow: hidden;
    background: var(--page-bg);
  }
  .sheet {
    width: 1200px; height: 1000px;
    display: flex; align-items: center; justify-content: center; gap: 40px;
  }
  .card {
    position: relative;
    width: 540px; height: 310px;
    border-radius: 4px;
    overflow: hidden;
    box-shadow: 0 10px 30px rgba(0,0,0,0.18);
  }

  /* Front */
  .card--front {
    background: radial-gradient(ellipse at 15% 0%, var(--blue-bright) 0%, var(--navy) 55%, var(--navy-deep) 100%);
    color: var(--paper);
  }
  .brand {
    display: flex; align-items: center; gap: 12px;
    font-family: "Cinzel", serif; font-weight: 500;
    letter-spacing: 0.06em;
  }
  .brand__dot {
    width: 26px; height: 26px; border-radius: 50%;
    background: var(--balloon-green);
    flex: none;
  }
  .card--front .brand {
    position: absolute; left: 50%; top: 118px; transform: translateX(-50%);
    font-size: 32px; white-space: nowrap; color: var(--paper);
  }
  .card--front .website {
    position: absolute; left: 0; right: 0; bottom: 62px;
    text-align: center;
    font-family: "Open Sans", sans-serif; font-size: 15px;
    letter-spacing: 0.12em; color: var(--soft-white);
  }

  /* Back */
  .card--back { background: var(--paper); }
  .card--back .band { position: absolute; inset: 0; }
  .card--back .brand {
    position: absolute; right: 44px; top: 48px;
    font-size: 23px; color: var(--navy);
  }
  .card--back .brand__dot { width: 20px; height: 20px; }
  .contact {
    position: absolute; right: 60px; top: 108px;
    font-family: "Open Sans", sans-serif; text-align: left;
  }
  .contact__name {
    font-weight: 600; font-size: 17px; letter-spacing: 0.04em;
    color: var(--name-green); margin-bottom: 8px;
  }
  .contact__line {
    font-size: 13px; letter-spacing: 0.06em; color: var(--ink-grey);
    line-height: 1.6;
  }
  .card--back .website {
    position: absolute; left: 34px; bottom: 30px;
    font-family: "Open Sans", sans-serif; font-size: 15px;
    letter-spacing: 0.12em; color: var(--paper);
  }
</style>
</head>
<body>
  <main class="sheet">
    <section class="card card--front" aria-label="Card front">
      <div class="brand"><span>Marigold Real Estate</span><span class="brand__dot"></span></div>
      <p class="website">www.marigoldhomes.com</p>
    </section>

    <section class="card card--back" aria-label="Card back">
      <svg class="band" viewBox="0 0 540 310" width="540" height="310" aria-hidden="true">
        <path d="M0 150 C 140 215, 330 250, 540 296 L540 310 L0 310 Z" fill="var(--navy-deep)"/>
        <path d="M0 147 C 140 212, 330 247, 540 293" fill="none" stroke="var(--name-green)" stroke-width="2"/>
      </svg>
      <div class="brand"><span>Marigold Real Estate</span><span class="brand__dot"></span></div>
      <div class="contact">
        <p class="contact__name">Alex Rowan</p>
        <p class="contact__line">5550 1234</p>
        <p class="contact__line">hello@marigoldhomes.com</p>
      </div>
      <p class="website">www.marigoldhomes.com</p>
    </section>
  </main>
</body>
</html>
```